Accounting firm needs a postcard design

We need a postcard design for our accounting office for a advertising campaign mailing we do yearly from a mail list we create. We are a full-service accounting office that has been in business for 35 years. I have attached our logo in different formats along with a document with a description of the services we provide. I have also attached my business card and the business card of our CPA. The business cards will have contact information for the postcard design. The contact email that will need to be on the postcard is contact@marlowtaxpartners.com.

```html
<!DOCTYPE html>
<html lang="en">
<head>
<meta charset="utf-8">
<title>Marlow Tax Partners – Postcard</title>
<link rel="stylesheet" href="https://fonts.googleapis.com/css2?family=Arimo:wght@400;700&family=Tinos:wght@700&display=swap">
<style>
  :root {
    --navy: #0c3868;
    --band-blue: #1a72b8;
    --brand-green: #5ab033;
    --ink-navy: #1b3d6e;
    --white: #ffffff;
    --rule-grey: #a9a9a9;
    --photo-top: #6f90ad;
    --photo-mid: #c8ccc8;
    --photo-low: #8a6a55;
  }
  * { box-sizing: border-box; margin: 0; padding: 0; }
  html, body { width: 1200px; height: 816px; overflow: hidden; background: var(--white); }
  .postcard { position: relative; width: 1200px; height: 816px; background: var(--white); font-family: "Arimo", Arial, sans-serif; }

  .promo-side { position: absolute; left: 0; top: 0; width: 600px; height: 816px; background: var(--navy); }
  .hero-photo {
    position: absolute; left: 0; top: 0; width: 600px; height: 300px;
    background: linear-gradient(160deg, var(--photo-top) 0%, var(--photo-mid) 45%, #b9c1bb 65%, var(--photo-low) 100%);
  }
  .price-badge {
    position: absolute; left: 424px; top: 104px; width: 188px; height: 188px; border-radius: 50%;
    background: var(--brand-green); color: var(--white);
    display: flex; align-items: center; justify-content: center; text-align: center;
    font-size: 21px; line-height: 26px;
  }
  .title-band {
    position: absolute; left: 0; top: 300px; width: 612px; height: 62px; background: var(--band-blue);
    display: flex; align-items: center; justify-content: center; padding-right: 12px;
  }
  .title-band h2 { font-family: "Tinos", "Times New Roman", serif; font-weight: 700; font-size: 35px; color: var(--white); letter-spacing: 0.3px; }

  .about-text {
    position: absolute; left: 62px; top: 400px; width: 480px;
    color: var(--white); font-size: 15.4px; line-height: 20.4px; text-align: center;
  }
  .cta { position: absolute; left: 0; width: 600px; text-align: center; color: var(--white); }
  .cta-line { top: 563px; font-size: 23px; }
  .cta-phone { top: 607px; font-size: 35px; }
  .cta-email { top: 655px; font-size: 23px; }
  .cta-web { top: 684px; font-size: 23px; }

  .brand-block { position: absolute; left: 620px; top: 154px; width: 380px; text-align: center; }
  .brand-name { font-family: "Tinos", "Times New Roman", serif; font-weight: 700; font-size: 21px; letter-spacing: 1.2px; color: var(--ink-navy); }
  .brand-services { margin-top: 3px; font-size: 10px; color: #222; }

  .stamp-box { position: absolute; left: 1020px; top: 40px; width: 132px; height: 154px; border: 2px solid var(--rule-grey); }
  .address-lines { position: absolute; left: 678px; top: 0; width: 444px; height: 816px; }
  .address-lines span { position: absolute; left: 0; width: 444px; height: 2px; background: var(--rule-grey); }
</style>
</head>
<body>
<div class="postcard">
  <section class="promo-side">
    <div class="hero-photo" role="img" aria-label="Photo of US dollar bills resting on a silver laptop keyboard"></div>
    <div class="price-badge">Full Service<br>Bookkeeping<br>Starting at<br>$400/mo.</div>
    <div class="title-band"><h2>WHO WE ARE?</h2></div>
    <p class="about-text">Our company has been providing tax and accounting services in Fort Worth and surrounding areas for the past 35 years. Our guiding philosophy has always been to provide our clients with per sonalized services tailored to their individual needs. Our firm has the knowledge and experience necessary to provide comprehensive accounting services to individuals and businesses in a broad range of industries.</p>
    <p class="cta cta-line">Contact us today for your no obligation quote!</p>
    <p class="cta cta-phone">(817) 555-0142</p>
    <p class="cta cta-email">contact@marlowtaxpartners.com</p>
    <p class="cta cta-web">www.marlowtaxpartners.com</p>
  </section>

  <div class="brand-block">
    <p class="brand-name">MARLOW TAX PARTNERS</p>
    <p class="brand-services">Tax Preparation&nbsp; I &nbsp;Bookkeeping&nbsp; I &nbsp;Payroll&nbsp; I &nbsp;Entity Formation</p>
  </div>

  <div class="stamp-box"></div>

  <div class="address-lines">
    <span style="top:421px"></span>
    <span style="top:517px"></span>
    <span style="top:613px"></span>
    <span style="top:709px"></span>
  </div>
</div>
</body>
</html>
```